I need a Billboard Design for our company called kelMARINDO.
I'm completely open for any design idea, but it must be professional and adventurous. The Billboard is 10ft high and 20ft wide.
Our Slogan is: "The ULTIMATE HELICOPTER DOORS-OFF Experience."
"Say YES to New Adventures"
Locations: SARASOTA | TAMPA | NAPLES
Prices Starting at $99.
Hotline: (844) KEL-MARI(ndo) (844) 535-6274
www.kelMARINDO.com
Target Market(s)
Aviation, Tourism
Industry/Entity Type
Tourism
Requirements
Must have
- The Design should match our website design at www.kelMARINDO.com
Please checkout the website for ideas. Thank you

```html
<!DOCTYPE html>
<html lang="en">
<head>
<meta charset="UTF-8">
<title>kelMARINDO Billboard</title>
<link rel="stylesheet" href="https://fonts.googleapis.com/css2?family=Bebas+Neue&family=Ubuntu:wght@400;500;700&display=swap">
<style>
  :root {
    --brand-blue: #1f78c1;
    --brand-blue-deep: #1a6aae;
    --board-white: #f1f2f4;
    --ink: #1c1d22;
    --ink-soft: #33363d;
    --stage: #dfe6ee;
    --photo-sky: #b9c7d2;
    --photo-mid: #6f7f8c;
    --photo-dark: #2c3a44;
  }
  * { box-sizing: border-box; margin: 0; padding: 0; }
  html, body { width: 1200px; height: 900px; overflow: hidden; }
  body { background: var(--stage); position: relative; font-family: "Ubuntu", sans-serif; }

  .billboard {
    position: absolute; left: 40px; top: 170px;
    width: 1120px; height: 560px;
    background: var(--board-white);
    overflow: hidden;
    box-shadow: 0 6px 24px rgba(20, 40, 70, 0.18);
  }
  .corner-band { position: absolute; left: 0; top: 0; width: 200px; height: 340px; }

  .brand { position: absolute; left: 150px; top: 110px; display: flex; align-items: center; gap: 14px; }
  .brand-dot { width: 26px; height: 26px; border-radius: 50%; background: var(--brand-blue); }
  .brand-name { font-family: "Ubuntu", sans-serif; font-weight: 500; font-size: 44px; color: var(--brand-blue); letter-spacing: 1px; }
  .brand-rule { position: absolute; left: 150px; top: 172px; width: 250px; height: 3px; background: var(--brand-blue); }

  .headline {
    position: absolute; left: 80px; top: 230px;
    font-family: "Bebas Neue", sans-serif; font-size: 62px; line-height: 0.95;
    color: var(--brand-blue); letter-spacing: 0.5px;
  }
  .subline {
    position: absolute; left: 80px; top: 352px;
    font-family: "Bebas Neue", sans-serif; font-size: 44px; color: var(--ink-soft);
  }

  .contact { position: absolute; left: 80px; top: 412px; }
  .contact-label { font-weight: 700; font-size: 22px; color: var(--brand-blue); margin-bottom: 4px; letter-spacing: 0.5px; }
  .contact-line { font-size: 24px; color: var(--ink); line-height: 1.15; letter-spacing: 0.5px; }
  .contact-web { font-size: 26px; font-weight: 700; color: var(--ink); letter-spacing: 2px; margin-top: 4px; }

  .photo {
    position: absolute; left: 600px; top: 60px; width: 460px; height: 440px;
    border-radius: 50% 0 50% 50%;
    background: linear-gradient(135deg, var(--photo-mid) 0%, var(--photo-sky) 45%, var(--photo-dark) 100%);
  }

  .price-badge {
    position: absolute; left: 935px; top: 110px; width: 118px; height: 118px;
    border-radius: 50%; background: var(--brand-blue); color: #fff;
    display: flex; flex-direction: column; align-items: center; justify-content: center;
    text-align: center;
  }
  .price-lead { font-size: 15px; line-height: 1.2; }
  .price-value { font-size: 36px; font-weight: 700; line-height: 1.1; }

  .locations { position: absolute; left: 690px; top: 478px; color: var(--ink); }
  .locations-label { font-size: 20px; letter-spacing: 2px; }
  .locations-list { font-size: 23px; font-weight: 700; letter-spacing: 2.5px; margin-top: 2px; }
</style>
</head>
<body>
  <main class="billboard">
    <svg class="corner-band" viewBox="0 0 200 340" aria-hidden="true">
      <path d="M0 0 H185 C140 110 80 230 0 335 Z" fill="var(--brand-blue)"/>
    </svg>

    <div class="brand">
      <span class="brand-dot"></span>
      <span class="brand-name">kelMARINDO</span>
    </div>
    <div class="brand-rule"></div>

    <h1 class="headline">The Ultimate Helicopter<br>Doors-Off Experience.</h1>
    <p class="subline">Say Yes to New Adventures.</p>

    <section class="contact">
      <p class="contact-label">Hotline</p>
      <p class="contact-line">(844) KEL-MARI(ndo)</p>
      <p class="contact-line">(844) 535-6274</p>
      <p class="contact-web">www.kelMARINDO.com</p>
    </section>

    <div class="photo" role="img" aria-label="Photo of two smiling passengers wearing headsets in an open-door helicopter above a city"></div>

    <div class="price-badge">
      <span class="price-lead">Prices<br>Starting at</span>
      <span class="price-value">$99</span>
    </div>

    <section class="locations">
      <p class="locations-label">Locations :</p>
      <p class="locations-list">SARASOTA | TAMPA | NAPLES</p>
    </section>
  </main>
</body>
</html>
```